Communication of Recommended Belief Letter

To Whom This May Concern,

My company's name is Brookfane LLC. I would like to send electronic messages to my clients. Therefore, I would like PixelForge to create a letterhead template to say Brookfane- without the LLC. My messages could extend up to 20 pages long. I would like something that is chic, fancy, and has creative designs. The background color should be white. The creative designs are open for suggestions without color restrictions. Font type and color are also open for suggestions. It may be what you believe best suite's the letterhead. I would like the letterhead to include the company logo. Please see attachment for file. Thank you.

Target Market(s)

working class American's

Industry/Entity Type

Communication

Contact Information for Business Card

The business card should be chic and fancy.

Font styles to use
Script

Requirements
Must have
• Company name: Brookfane LLC
• Company symbol: Please see attachment
• Name: Moriel Haskins
• Title: President
• Company website: www.brookfanellc-example.com
Nice to have
• Open for suggestions

```html
<!DOCTYPE html>
<html lang="en">
<head>
<meta charset="utf-8">
<title>Brookfane Letterhead</title>
<link href="https://fonts.googleapis.com/css2?family=Open+Sans:ital,wght@0,400;0,700;1,400&display=swap" rel="stylesheet">
<style>
  :root {
    --backdrop: #c2cfcf;
    --paper: #ffffff;
    --yellow-deep: #ebcc0a;
    --yellow-bright: #fff700;
    --stripe: #e3e8ec;
    --gold: #a87c16;
    --ink: #111111;
    --title-yellow: #e8c800;
  }
  * { margin: 0; padding: 0; box-sizing: border-box; }
  html, body {
    width: 1200px;
    height: 1200px;
    overflow: hidden;
    background: var(--backdrop);
    font-family: "Open Sans", Arial, sans-serif;
  }
  .canvas {
    position: relative;
    width: 1200px;
    height: 1200px;
    background: var(--backdrop);
  }
  .letterhead {
    position: absolute;
    left: 182px;
    top: 60px;
    width: 835px;
    height: 1081px;
    background: var(--paper);
    overflow: hidden;
  }
  .wave-art {
    position: absolute;
    inset: 0;
    width: 100%;
    height: 100%;
  }
  .brand {
    position: absolute;
    top: 218px;
    left: 0;
    width: 100%;
    display: flex;
    justify-content: center;
    align-items: center;
    gap: 18px;
  }
  .brand-dot {
    width: 40px;
    height: 40px;
    border-radius: 50%;
    background: var(--gold);
  }
  .brand-name {
    font-size: 44px;
    font-weight: 400;
    letter-spacing: 2px;
    color: var(--gold);
    line-height: 1;
  }
  .signatory {
    position: absolute;
    right: 27px;
    top: 876px;
    text-align: right;
    font-size: 27px;
    line-height: 33px;
    letter-spacing: 0.5px;
  }
  .signatory-name {
    font-style: italic;
    color: var(--ink);
  }
  .signatory-title {
    font-weight: 700;
    color: var(--title-yellow);
  }
  .website {
    position: absolute;
    top: 984px;
    left: 0;
    width: 100%;
    text-align: center;
    font-size: 22px;
    color: var(--ink);
  }
</style>
</head>
<body>
<div class="canvas">
  <div class="letterhead">
    <svg class="wave-art" viewBox="0 0 870 1126" preserveAspectRatio="none" aria-hidden="true">
      <defs>
        <linearGradient id="topGlow" x1="0" y1="0" x2="1" y2="0">
          <stop offset="0" stop-color="var(--yellow-deep)"/>
          <stop offset="0.55" stop-color="#f3e006"/>
          <stop offset="0.8" stop-color="var(--yellow-bright)"/>
          <stop offset="1" stop-color="#f6ec02"/>
        </linearGradient>
        <linearGradient id="bandGlow" x1="0" y1="0" x2="1" y2="0">
          <stop offset="0" stop-color="var(--yellow-deep)"/>
          <stop offset="0.6" stop-color="#ecd30a"/>
          <stop offset="0.85" stop-color="#fbf100"/>
          <stop offset="1" stop-color="var(--yellow-deep)"/>
        </linearGradient>
        <filter id="softShadow" x="-10%" y="-50%" width="120%" height="200%">
          <feGaussianBlur stdDeviation="9"/>
        </filter>
      </defs>

      <!-- header shadow -->
      <path d="M0 232 C120 185 250 130 380 128 C560 130 700 180 870 192 L870 150 L0 150 Z" fill="#9a9a9a" opacity="0.35" filter="url(#softShadow)"/>
      <!-- header lower band -->
      <path d="M0 0 H870 V183 C700 178 560 122 380 120 C250 120 120 175 0 223 Z" fill="url(#bandGlow)"/>
      <!-- header light stripe -->
      <path d="M0 0 H870 V160 C650 150 500 78 380 70 C290 66 150 92 0 140 Z" fill="var(--stripe)"/>
      <!-- header top band -->
      <path d="M0 0 H870 V146 C600 135 450 52 330 45 C250 42 150 70 0 115 Z" fill="url(#topGlow)"/>

      <!-- footer shadow -->
      <path d="M0 1030 C200 1030 350 1060 480 1060 C640 1055 760 1010 870 978 L870 1040 L0 1060 Z" fill="#b5b5b5" opacity="0.35" filter="url(#softShadow)"/>
      <!-- footer light stripe -->
      <path d="M0 1040 C180 1030 330 1065 470 1065 C640 1060 760 1015 870 985 V1126 H0 Z" fill="var(--stripe)"/>
      <!-- footer yellow band -->
      <path d="M0 1052 C160 1048 300 1092 430 1094 C600 1096 740 1060 870 1045 V1126 H0 Z" fill="var(--yellow-deep)"/>
    </svg>

    <div class="brand">
      <span class="brand-dot"></span>
      <span class="brand-name">BROOKFANE</span>
    </div>

    <div class="signatory">
      <p class="signatory-name">Moriel Haskins</p>
      <p class="signatory-title">President</p>
    </div>

    <p class="website">www.brookfanellc-example.com</p>
  </div>
</div>
</body>
</html>
```